Candle Labels for 9 oz tumbler soy candles

Looking for new label design for my candle business. Currently, using a label I designed that needs to be more professional rather than looking homemade. Wanting a professional, clean looking label that enhances my product line. My candle tumblers are white and at times I also use tin containers for my candles so wanting something that will provide a modern/elegant feel to them

Industry/Entity Type

Business

Font styles to use
Decorative
Script

Colors

Designer to choose colors to be used in the design.

Requirements
Must have
• My logo, net weight 9 oz, Space for the name of the Candle (one example is Amber Hollow
• Looking for something sleek and clean looking, no clutter
Nice to have
• website url www.8brook5candleco.shopvale.com, words "Soy Candle" on the label

```html
<!DOCTYPE html>
<html lang="en">
<head>
<meta charset="utf-8">
<title>Amber Hollow Soy Candle Label</title>
<link href="https://fonts.googleapis.com/css2?family=Kaushan+Script&family=Cinzel:wght@700&family=Roboto:wght@400;500&display=swap" rel="stylesheet">
<style>
  :root {
    --green: #4e6b5e;
    --amber: #f5a938;
    --paper: #ffffff;
    --backdrop: #ffffff;
  }
  html, body {
    margin: 0;
    padding: 0;
    width: 1200px;
    height: 922px;
    overflow: hidden;
    background: var(--backdrop);
  }
  .canvas {
    position: relative;
    width: 1200px;
    height: 922px;
  }
  .label {
    position: absolute;
    left: 250px;
    top: 111px;
    width: 700px;
    height: 700px;
  }
  .ring-green { fill: none; stroke: var(--green); stroke-width: 5; }
  .ring-amber { fill: none; stroke: var(--amber); stroke-width: 5; }
  .brand-name {
    font-family: "Roboto", sans-serif;
    font-weight: 500;
    font-size: 46px;
    fill: var(--green);
  }
  .brand-dot { fill: var(--amber); }
  .scent-name {
    font-family: "Kaushan Script", cursive;
    font-size: 86px;
    fill: var(--green);
  }
  .ribbon { fill: var(--green); }
  .ribbon-text {
    font-family: "Cinzel", serif;
    font-weight: 700;
    font-size: 44px;
    letter-spacing: 2px;
    fill: var(--amber);
  }
  .site-url {
    font-family: "Roboto", sans-serif;
    font-weight: 500;
    font-size: 22px;
    fill: var(--green);
  }
  .net-weight {
    font-family: "Roboto", sans-serif;
    font-weight: 400;
    font-size: 28px;
    fill: var(--amber);
  }
</style>
</head>
<body>
<main class="canvas">
  <svg class="label" viewBox="0 0 700 700" xmlns="http://www.w3.org/2000/svg">
    <circle cx="350" cy="350" r="347" fill="var(--paper)"/>
    <!-- double ring: colours swap at the midline -->
    <path class="ring-green" d="M3,350 A347,347 0 0 1 697,350"/>
    <path class="ring-amber" d="M15,350 A335,335 0 0 1 685,350"/>
    <path class="ring-amber" d="M3,350 A347,347 0 0 0 697,350"/>
    <path class="ring-green" d="M15,350 A335,335 0 0 0 685,350"/>

    <g class="brand">
      <circle class="brand-dot" cx="138" cy="180" r="11"/>
      <text class="brand-name" x="365" y="197" text-anchor="middle">8Brook5 Candle Co.</text>
    </g>

    <text class="scent-name" x="350" y="372" text-anchor="middle">Amber Hollow</text>

    <g class="soy-ribbon">
      <path class="ribbon" d="M96,428 L152,436 L152,492 L112,484 L132,460 Z"/>
      <path class="ribbon" d="M570,404 L628,396 L606,424 L638,456 L580,462 Z"/>
      <path class="ribbon" d="M140,432 Q360,462 585,404 L590,462 Q360,516 148,490 Z"/>
      <text class="ribbon-text" x="364" y="474" text-anchor="middle" transform="rotate(-6 364 460)">SOY CANDLE</text>
    </g>

    <text class="site-url" x="350" y="560" text-anchor="middle">www.8brook5candleco.shopvale.com</text>
    <text class="net-weight" x="350" y="620" text-anchor="middle">Net weight 9 oz</text>
  </svg>
</main>
</body>
</html>
```